Dermavive Label Design

We need a label design for our cream dispenser. Its a cream against acne called Dermavive, Works with its active ingredients of silver and oxygen. We are looking for a flashy / colorful and modern design .
Updates

Low design quality

Target Market(s)

young people / People with acne

Industry/Entity Type

Skin Care Product

Colors

Designer to choose colors to be used in the design.

Requirements
Must have
• be modern, Colours
• -THE DESIGN NEEDS TO BE 10,7x7 , ITS 1 BIG STICKER THAT RAPS AROUND THE BOTTLE

```html
<!DOCTYPE html>
<html lang="en">
<head>
<meta charset="utf-8">
<title>Dermavive Acne Repair &amp; Care Label</title>
<link href="https://fonts.googleapis.com/css2?family=Montserrat:wght@400;500;600&display=swap" rel="stylesheet">
<style>
  :root {
    --page-bg: #eef1f2;
    --silver-light: #f7f7f7;
    --silver-mid: #dcdcdc;
    --silver-dark: #b9b9b9;
    --teal: #22bcc2;
    --teal-text: #1fb3b9;
    --graphite: #5b5d60;
    --white: #ffffff;
    --cream-shadow: #e4e6e7;
  }
  * { margin: 0; padding: 0; box-sizing: border-box; }
  html, body {
    width: 1200px;
    height: 1200px;
    overflow: hidden;
  }
  body {
    background: var(--page-bg);
    font-family: "Montserrat", sans-serif;
    position: relative;
  }
  .label {
    position: absolute;
    left: 339px;
    top: 84px;
    width: 522px;
    height: 1032px;
    background: var(--white);
    overflow: hidden;
  }
  .label-shapes,
  .label-artwork {
    position: absolute;
    left: 0;
    top: 0;
    width: 522px;
    height: 1032px;
  }
  .maker-mark {
    position: absolute;
    top: 92px;
    left: 0;
    width: 100%;
    display: flex;
    justify-content: center;
    align-items: center;
    gap: 12px;
  }
  .maker-mark__square {
    width: 22px;
    height: 22px;
    background: var(--graphite);
  }
  .maker-mark__name {
    font-weight: 500;
    font-size: 34px;
    color: var(--graphite);
    letter-spacing: 1px;
  }
  .product-name {
    position: absolute;
    top: 188px;
    left: 0;
    width: 100%;
    text-align: center;
    font-weight: 600;
    font-size: 58px;
    letter-spacing: 5px;
    color: var(--graphite);
  }
  .product-claim {
    position: absolute;
    top: 430px;
    left: 0;
    width: 100%;
    text-align: center;
    font-weight: 500;
    font-size: 46px;
    line-height: 64px;
    color: var(--white);
  }
  .product-tagline {
    position: absolute;
    top: 870px;
    left: 0;
    width: 100%;
    text-align: center;
    font-weight: 500;
    font-size: 27px;
    line-height: 38px;
    color: var(--teal-text);
  }
  .product-volume {
    position: absolute;
    top: 970px;
    left: 0;
    width: 100%;
    text-align: center;
    font-weight: 500;
    font-size: 18px;
    color: var(--teal-text);
  }
</style>
</head>
<body>
  <div class="label">
    <svg class="label-shapes" viewBox="0 0 522 1032" aria-hidden="true">
      <defs>
        <linearGradient id="silverBand" x1="0" y1="0" x2="1" y2="0">
          <stop offset="0" stop-color="var(--silver-dark)"/>
          <stop offset="0.25" stop-color="var(--silver-light)"/>
          <stop offset="0.6" stop-color="var(--silver-light)"/>
          <stop offset="1" stop-color="var(--silver-dark)"/>
        </linearGradient>
        <linearGradient id="silverEdge" x1="0" y1="0" x2="1" y2="0">
          <stop offset="0" stop-color="#a9a9a9"/>
          <stop offset="0.5" stop-color="#d6d6d6"/>
          <stop offset="1" stop-color="#a9a9a9"/>
        </linearGradient>
      </defs>
      <rect class="silver-band" x="0" y="0" width="522" height="340" fill="url(#silverBand)"/>
      <path class="silver-edge" d="M0,300 Q261,240 522,300 L522,330 Q261,268 0,330 Z" fill="url(#silverEdge)"/>
      <path class="teal-band" d="M0,330 Q261,268 522,330 L522,720 L0,720 Z" fill="var(--teal)"/>
    </svg>
    <svg class="label-artwork" viewBox="0 0 522 1032" role="img" aria-label="White feather resting on rippling cream">
      <defs>
        <radialGradient id="creamRipple" cx="0.5" cy="0.22" r="0.75">
          <stop offset="0" stop-color="var(--cream-shadow)"/>
          <stop offset="0.45" stop-color="var(--white)"/>
          <stop offset="1" stop-color="var(--white)"/>
        </radialGradient>
      </defs>
      <path d="M0,700 Q261,672 522,700 L522,1032 L0,1032 Z" fill="url(#creamRipple)"/>
    </svg>

    <div class="maker-mark">
      <span class="maker-mark__square"></span>
      <span class="maker-mark__name">Nova Lab</span>
    </div>
    <h1 class="product-name">Dermavive</h1>
    <p class="product-claim">ACNE REPAIR<br>&amp; CARE</p>
    <p class="product-tagline">LOREM IPSUM<br>DOLOR SIT AMET</p>
    <p class="product-volume">100 ML</p>
  </div>
</body>
</html>
```